A layout of a webpage for oil trade platform

I would like to have a desgin of one page webpage (with section scrollling dowin) that woulf present the new product i.e. oil trade platform for wholesale buyers and sellers.
Layout should consist of the sections similar to the given at: https://strona.trawomirek.pl/modul-planowania-spotkan
However oil industy require more colors and more photo stories than here for doctor.
I. I woul imagine at first below menu a slider with brueg information about the product and its advantages with "more" button next to the prict screen of our platform on different displays (PC and mobile).
II. Bellow the slider I would imagine icons correspoing to the advantages of that plaftorm:
1. Purchase/sale process automation 24/7
2. Access to the best deals
3. Electronic offerings and orderings
4. Transaction status monitoring
5. Data and transaction security
II A) (optional):
In near future we would like to prepare a short video presenation. Hence please prepare a place to display that element here.
At the moment alternatvily please prepare a How it works section that would explan the platform operating process
III. Next secion is about benefits for Oil Purchaser
It can be done either by icons of by text and corresponding grahip for while section.
Benefits:
- Access to cheaper oil
- Convenience of online orders
- Possibility to compare prices on the market
- Transaction history
- Order status monitoring
- Seccurity and transparency of purchase
IV. Next seciont is about benefits for Oil Seller
Benefits:
- New sale channel
- Attracting new clients
- More oil sold
- Transaction security
- Possibility to integrate with distribution infrastructure and logistits for more efficient automation.
V. Contact form
VI. Footer
I would need a layout that that will correspond to the very dynamic logo but I would expect also a clean form, smoth and modern. It has to be proffessional layout with more corporate character.
It can use a paralax features if needed.
Attachments:
- logo design
- platfrom print screen
Industry/Entity Type
Oil And Gas
Number of Pages Required
1 page

```html
<!DOCTYPE html>
<html lang="en">
<head>
<meta charset="utf-8">
<title>Crudexa — Oil Trade Platform</title>
<link rel="stylesheet" href="https://fonts.googleapis.com/css2?family=Montserrat:wght@500;600;700&family=Lato:wght@400;700&display=swap">
<style>
:root{
  --orange:#f26522;
  --orange-soft:#f58a4e;
  --navy:#13234b;
  --navy-deep:#0f1c3d;
  --ink:#333333;
  --grey:#8b8b8b;
  --line:#d6d6d6;
  --white:#ffffff;
  --head:"Montserrat",sans-serif;
  --body:"Lato",sans-serif;
}
*{box-sizing:border-box;margin:0;padding:0}
html,body{width:1200px;height:3125px;overflow:hidden}
body{position:relative;background:var(--white);font-family:var(--body);color:var(--ink)}
.abs{position:absolute}

/* header */
.site-header{position:absolute;top:0;left:0;width:1200px;height:98px;background:var(--white)}
.brand{position:absolute;left:162px;top:22px;display:flex;align-items:center;gap:12px}
.brand-mark{width:46px;height:46px;border-radius:50%;background:var(--orange)}
.brand-name{font-family:var(--body);font-weight:700;font-size:30px;color:var(--navy);letter-spacing:1px}
.menu-toggle{position:absolute;left:1000px;top:33px;width:38px;height:34px;border:2px solid var(--navy);border-radius:5px}
.menu-toggle span{position:absolute;left:9px;width:16px;height:3px;background:var(--navy)}

/* hero */
.hero{position:absolute;top:98px;left:0;width:1200px;height:485px;
  background:linear-gradient(180deg,#3f6da6 0%,#6e92c0 35%,#2f5589 62%,#0f2c5c 100%)}
.hero-photo{position:absolute;left:640px;top:0;width:480px;height:400px;
  background:radial-gradient(ellipse at center,rgba(60,70,90,.55),rgba(60,70,90,0) 70%)}
.hero-title{position:absolute;left:162px;top:190px;font-family:var(--head);font-weight:600;font-size:29px;color:var(--white)}
.hero-text{position:absolute;left:162px;top:232px;width:445px;font-size:15px;line-height:21px;color:var(--white)}

/* section heading */
.section-title{position:absolute;left:0;width:1200px;text-align:center;font-family:var(--head);font-weight:700;font-size:31px;color:var(--navy)}
.section-title em{font-style:normal;color:var(--orange)}
.divider{position:absolute;left:312px;width:576px;height:20px}
.divider::before{content:"";position:absolute;left:0;right:0;top:10px;height:1px;background:var(--line)}
.divider::after{content:"";position:absolute;left:281px;top:3px;width:14px;height:14px;border-radius:50%;border:2px solid #c8c8c8;background:var(--white)}
.divider.on-dark::before{background:rgba(255,255,255,.45)}
.divider.on-dark::after{background:#2e3468;border-color:rgba(255,255,255,.7)}

/* welcome */
.welcome-text{position:absolute;left:194px;top:718px;width:814px;text-align:center;font-size:13px;line-height:21px}
.advantages-title{position:absolute;left:0;width:1200px;top:803px;text-align:center;font-weight:700;font-size:16px;color:var(--navy)}
.advantage{position:absolute;top:854px;width:180px;text-align:center}
.advantage-icon{width:116px;height:116px;margin:0 auto;border-radius:50%;border:4px solid var(--navy);background:#e4e4e4;display:flex;align-items:center;justify-content:center}
.advantage.is-active .advantage-icon{border-color:var(--orange);background:var(--orange)}
.advantage-label{margin-top:22px;height:52px;font-size:14px;line-height:20px;color:var(--ink)}
.more-btn{display:block;margin:0 auto;width:83px;height:29px;line-height:29px;font-size:13px;color:var(--white);background:var(--grey);letter-spacing:.5px}
.advantage.is-active .more-btn{background:var(--orange)}

/* video */
.video{position:absolute;top:1127px;left:0;width:1200px;height:481px;
  background:linear-gradient(180deg,#3a3c7a 0%,#2c2d64 55%,#161a3a 100%)}
.video .section-title{color:var(--white);top:48px}
.video-frame{position:absolute;left:412px;top:152px;width:388px;height:296px;border-radius:16px;
  background:linear-gradient(180deg,#2a2a2a,#111)}

/* how it works */
.step{position:absolute;top:1758px;width:210px;text-align:center}
.step-icon{width:100px;height:100px;margin:0 auto;border-radius:50%;background:var(--orange);display:flex;align-items:center;justify-content:center}
.step-title{margin-top:20px;font-weight:700;font-size:16px;color:var(--orange)}
.step-text{margin-top:4px;font-size:13px;line-height:18px}

/* benefits */
.benefit-panel{position:absolute;width:600px;height:350px}
.benefit-panel h3{position:absolute;font-family:var(--head);font-weight:600;font-size:21px;color:var(--white)}
.benefit-list{position:absolute;list-style:none;color:var(--white);font-size:13px}
.benefit-list li{position:relative;padding-left:24px;line-height:29px}
.benefit-list li.two-line{line-height:18px;margin-top:6px}
.benefit-list svg{position:absolute;left:0;top:7px}
.benefit-list li.two-line svg{top:2px}
.panel-divider{position:absolute;height:20px}
.panel-divider::before{content:"";position:absolute;left:0;right:0;top:10px;height:1px;background:rgba(255,255,255,.7)}
.panel-divider::after{content:"";position:absolute;left:0;top:3px;width:14px;height:14px;border-radius:50%;border:2px solid var(--white)}

/* contact */
.field{position:absolute;border:1px solid #cfcfcf;background:var(--white);font-size:11px;color:#666;padding:9px 12px}
.submit-btn{position:absolute;left:515px;top:2996px;width:170px;height:27px;background:var(--navy);color:var(--white);text-align:center;line-height:27px;font-size:13px;letter-spacing:.5px}

/* footer */
.site-footer{position:absolute;top:3075px;left:0;width:1200px;height:50px;background:var(--navy-deep)}
.copyright{position:absolute;left:162px;top:17px;font-size:13px;color:var(--white)}
.social{position:absolute;top:10px;width:30px;height:30px;border-radius:50%;background:var(--orange)}
</style>
</head>
<body>

<header class="site-header">
  <div class="brand"><span class="brand-mark"></span><span class="brand-name">CRUDEXA</span></div>
  <div class="menu-toggle" aria-label="Menu">
    <span style="top:8px"></span><span style="top:14px"></span><span style="top:20px"></span>
  </div>
</header>

<section class="hero" role="img" aria-label="Offshore oil platform at sea under a blue cloudy sky">
  <div class="hero-photo"></div>
  <h1 class="hero-title">TRADE WITH CONFIDENCE</h1>
  <p class="hero-text">Lorem ipsum dolor sit amet, consectetuer adipiscing elit, sed diam nonummy nibh euismod tincidunt ut laoreet dolore magna aliquam erat volutpat.</p>
</section>

<section class="welcome">
  <h2 class="section-title" style="top:628px">WELCOME TO <em>CRUDEXA</em></h2>
  <div class="divider" style="top:680px"></div>
  <p class="welcome-text">Lorem ipsum dolor sit amet, consectetuer adipiscing elit, sed diam nonummy nibh euismod tincidunt ut laoreet dolore magna aliquam erat volutpat. Ut wisi enim ad minim veniam, quis nostrud exerci tation ullamcorper suscipit lobortis nisl ut aliquip ex ea commodo consequat. Duis autem vel eum iriure dolor in hendrerit in vulputate velit esse .</p>
  <h3 class="advantages-title">Advantages of Our Portal</h3>

  <div class="advantage is-active" style="left:154px">
    <div class="advantage-icon">
      <svg width="70" height="70" viewBox="0 0 70 70" fill="none" stroke="#fff" stroke-width="3"><circle cx="35" cy="35" r="28"/><text x="35" y="42" text-anchor="middle" fill="#fff" stroke="none" font-family="Lato,sans-serif" font-size="20" font-weight="700">24/7</text></svg>
    </div>
    <div class="advantage-label">Purchase/sale Process<br>Automation 24/7</div>
    <span class="more-btn">MORE</span>
  </div>
  <div class="advantage" style="left:331px">
    <div class="advantage-icon">
      <svg width="56" height="56" viewBox="0 0 56 56" fill="#13234b"><rect x="6" y="24" width="10" height="24" rx="2"/><path d="M20 24 L30 8 Q35 6 35 12 L33 22 H46 Q51 23 50 28 L46 44 Q44 48 40 48 H20 Z"/></svg>
    </div>
    <div class="advantage-label">Access to the Best<br>Deals</div>
    <span class="more-btn">MORE</span>
  </div>
  <div class="advantage" style="left:510px">
    <div class="advantage-icon">
      <svg width="56" height="56" viewBox="0 0 56 56" fill="none" stroke="#13234b" stroke-width="4"><rect x="6" y="8" width="44" height="30" rx="3"/><path d="M28 38 V46 M18 48 H38"/></svg>
    </div>
    <div class="advantage-label">Electronic Offerings<br>and Orderings</div>
    <span class="more-btn">MORE</span>
  </div>
  <div class="advantage" style="left:687px">
    <div class="advantage-icon">
      <svg width="56" height="56" viewBox="0 0 56 56" fill="none" stroke="#13234b" stroke-width="4"><rect x="14" y="18" width="28" height="20" rx="2"/><circle cx="28" cy="28" r="5"/><path d="M8 14 A22 22 0 0 1 44 8 M48 42 A22 22 0 0 1 12 48"/><path d="M40 4 L44 8 L39 12 M16 44 L12 48 L17 52"/></svg>
    </div>
    <div class="advantage-label">Transaction Status<br>Monitoring</div>
    <span class="more-btn">MORE</span>
  </div>
  <div class="advantage" style="left:864px">
    <div class="advantage-icon">
      <svg width="56" height="56" viewBox="0 0 56 56" fill="none" stroke="#13234b" stroke-width="4"><rect x="16" y="6" width="24" height="44" rx="4"/><path d="M24 42 H32"/></svg>
    </div>
    <div class="advantage-label">Data and Transaction<br>Security</div>
    <span class="more-btn">MORE</span>
  </div>
</section>

<section class="video" role="img" aria-label="Industrial plant at dusk with hands holding a tablet playing the platform video">
  <h2 class="section-title">OUR VIDEO</h2>
  <div class="divider on-dark" style="top:96px"></div>
  <div class="video-frame"></div>
</section>

<section class="how-it-works">
  <h2 class="section-title" style="top:1653px">How <em>It</em> Works</h2>
  <div class="divider" style="top:1704px"></div>

  <svg class="abs" style="left:330px;top:1770px" width="560" height="60" viewBox="0 0 560 60" fill="none" stroke="#999" stroke-width="1.5" stroke-dasharray="3 4">
    <path d="M10 20 Q50 0 96 26"/><path d="M90 20 L96 26 L88 28" stroke-dasharray="none"/>
    <path d="M225 30 Q265 50 310 30"/><path d="M303 28 L310 30 L305 36" stroke-dasharray="none"/>
    <path d="M440 20 Q480 0 525 26"/><path d="M519 20 L525 26 L517 28" stroke-dasharray="none"/>
  </svg>

  <div class="step" style="left:166px">
    <div class="step-icon"><svg width="56" height="56" viewBox="0 0 56 56" fill="none" stroke="#fff" stroke-width="3"><circle cx="26" cy="30" r="18"/><path d="M8 30 H44 M26 12 V48 M14 18 Q26 26 38 18 M14 42 Q26 34 38 42"/><path d="M42 4 A8 8 0 0 1 50 12 Q50 18 42 26 Q34 18 34 12 A8 8 0 0 1 42 4 Z" fill="#f26522"/></svg></div>
    <div class="step-title">Portals</div>
    <p class="step-text">Lorem ipsum dolor sit amet, consectetuer adipiscing elit, sed diam nonummy nibh euismod tincidunt ut laoreet</p>
  </div>
  <div class="step" style="left:382px">
    <div class="step-icon"><svg width="56" height="56" viewBox="0 0 56 56" fill="none" stroke="#fff" stroke-width="4"><circle cx="32" cy="22" r="14"/><path d="M22 32 L8 48" stroke-width="6" stroke-linecap="round"/></svg></div>
    <div class="step-title">Enterprise Search</div>
    <p class="step-text">Lorem ipsum dolor sit amet, consectetuer adipiscing elit, sed diam nonummy nibh euismod tincidunt ut laoreet</p>
  </div>
  <div class="step" style="left:603px">
    <div class="step-icon"><svg width="56" height="56" viewBox="0 0 56 56" fill="#fff"><rect x="8" y="8" width="16" height="12" rx="2"/><rect x="32" y="8" width="16" height="12" rx="2"/><rect x="12" y="26" width="8" height="22"/><rect x="36" y="26" width="8" height="22"/><rect x="20" y="30" width="16" height="4"/></svg></div>
    <div class="step-title">Collaboration</div>
    <p class="step-text">Lorem ipsum dolor sit amet, consectetuer adipiscing elit, sed diam nonummy nibh euismod tincidunt ut laoreet</p>
  </div>
  <div class="step" style="left:822px">
    <div class="step-icon"><svg width="56" height="56" viewBox="0 0 56 56" fill="#fff"><rect x="8" y="36" width="7" height="12"/><rect x="19" y="28" width="7" height="20"/><rect x="30" y="22" width="7" height="26"/><rect x="41" y="14" width="7" height="34"/><path d="M8 28 L22 16 L30 20 L44 6" fill="none" stroke="#fff" stroke-width="3"/><path d="M38 5 H46 V13" fill="none" stroke="#fff" stroke-width="3"/></svg></div>
    <div class="step-title">Business Intelligence</div>
    <p class="step-text">Lorem ipsum dolor sit amet, consectetuer adipiscing elit, sed diam nonummy nibh euismod tincidunt ut laoreet</p>
  </div>
</section>

<section class="benefits">
  <div class="benefit-panel" style="left:0;top:2015px;background:var(--orange)">
    <h3 style="left:160px;top:50px">Benefits for Oil Purchaser</h3>
    <div class="panel-divider" style="left:160px;top:94px;width:298px"></div>
    <ul class="benefit-list" style="left:160px;top:128px">
      <li><svg width="14" height="14" viewBox="0 0 14 14" fill="none" stroke="#fff" stroke-width="1.6"><rect x="1" y="1" width="12" height="12"/><path d="M3.5 7 L6 9.5 L11 3.5"/></svg>Access to cheaper oil</li>
      <li><svg width="14" height="14" viewBox="0 0 14 14" fill="none" stroke="#fff" stroke-width="1.6"><rect x="1" y="1" width="12" height="12"/><path d="M3.5 7 L6 9.5 L11 3.5"/></svg>Convenience of online orders</li>
      <li><svg width="14" height="14" viewBox="0 0 14 14" fill="none" stroke="#fff" stroke-width="1.6"><rect x="1" y="1" width="12" height="12"/><path d="M3.5 7 L6 9.5 L11 3.5"/></svg>Possibility to compare prices on the market</li>
      <li><svg width="14" height="14" viewBox="0 0 14 14" fill="none" stroke="#fff" stroke-width="1.6"><rect x="1" y="1" width="12" height="12"/><path d="M3.5 7 L6 9.5 L11 3.5"/></svg>Transaction history</li>
      <li><svg width="14" height="14" viewBox="0 0 14 14" fill="none" stroke="#fff" stroke-width="1.6"><rect x="1" y="1" width="12" height="12"/><path d="M3.5 7 L6 9.5 L11 3.5"/></svg>Order status monitoring</li>
      <li><svg width="14" height="14" viewBox="0 0 14 14" fill="none" stroke="#fff" stroke-width="1.6"><rect x="1" y="1" width="12" height="12"/><path d="M3.5 7 L6 9.5 L11 3.5"/></svg>Security and transparency of purchase</li>
    </ul>
  </div>
  <div class="benefit-panel" style="left:600px;top:2015px;background:linear-gradient(180deg,#6d8fbf 0%,#8fa7c9 45%,#3d4a5e 100%)" role="img" aria-label="Offshore drilling platform with cranes against a blue sky"></div>

  <div class="benefit-panel" style="left:0;top:2365px;height:347px;background:linear-gradient(135deg,#c9ccce 0%,#8e9396 50%,#4a4f53 100%)" role="img" aria-label="Industrial pipeline with a pressure gauge"></div>
  <div class="benefit-panel" style="left:600px;top:2365px;height:347px;background:var(--navy)">
    <h3 style="left:25px;top:52px">Benefits for Oil Sellers</h3>
    <div class="panel-divider" style="left:25px;top:94px;width:298px"></div>
    <ul class="benefit-list" style="left:25px;top:126px;width:300px">
      <li><svg width="14" height="14" viewBox="0 0 14 14" fill="none" stroke="#fff" stroke-width="1.6"><rect x="1" y="1" width="12" height="12"/><path d="M3.5 7 L6 9.5 L11 3.5"/></svg>New sale channel</li>
      <li><svg width="14" height="14" viewBox="0 0 14 14" fill="none" stroke="#fff" stroke-width="1.6"><rect x="1" y="1" width="12" height="12"/><path d="M3.5 7 L6 9.5 L11 3.5"/></svg>Attracting new clients</li>
      <li><svg width="14" height="14" viewBox="0 0 14 14" fill="none" stroke="#fff" stroke-width="1.6"><rect x="1" y="1" width="12" height="12"/><path d="M3.5 7 L6 9.5 L11 3.5"/></svg>More oil sold</li>
      <li><svg width="14" height="14" viewBox="0 0 14 14" fill="none" stroke="#fff" stroke-width="1.6"><rect x="1" y="1" width="12" height="12"/><path d="M3.5 7 L6 9.5 L11 3.5"/></svg>Transaction security</li>
      <li class="two-line"><svg width="14" height="14" viewBox="0 0 14 14" fill="none" stroke="#fff" stroke-width="1.6"><rect x="1" y="1" width="12" height="12"/><path d="M3.5 7 L6 9.5 L11 3.5"/></svg>Possibility to integrate with distribution infrastructure and logistics for more efficient automation.</li>
    </ul>
  </div>
</section>

<section class="contact">
  <h2 class="section-title" style="top:2761px">CONTACT <em>US</em></h2>
  <div class="divider" style="top:2813px"></div>
  <div class="field" style="left:262px;top:2852px;width:330px;height:35px">Name*</div>
  <div class="field" style="left:262px;top:2898px;width:330px;height:35px">Email*</div>
  <div class="field" style="left:262px;top:2943px;width:330px;height:35px">Phone*</div>
  <div class="field" style="left:608px;top:2852px;width:330px;height:123px">Message*</div>
  <div class="submit-btn">SUBMIT</div>
</section>

<footer class="site-footer">
  <p class="copyright">Copyright © 2016 Crudexa Energy. All Rights Reserved.</p>
  <span class="social" style="left:929px"></span>
  <span class="social" style="left:966px"></span>
  <span class="social" style="left:1006px"></span>
</footer>

</body>
</html>
```